International Employee Benefits

Create website including logo for Halvorsen Global
Specialising in setting up and managing employee benefits for multi-national companies
Should be professional and simple to navigate
Updates

Company name is Halvorsen Global

Please ensure the following is adhered to :

Page size - 950 pixels wide

If you plan to use a texture or picture background please ensure these are tiled so that the left edge matches the right edge like wallpaper.

The home page should have the logo at the top left of the screen followed by tabs "About Us", "Resources" "Expertise" "References" "Contact Us"
Perhaps there can also be an image on the home page, something that signifies global success??

The wording on the home page should be:

 Halvorsen Global brings a results oriented approach partnering with clients in mapping out customized strategies that meet their international objectives that save time and money and leaves an established process in place.  The client is supported with a high touch, one point of contact, that bring solutions to complex problems

 

Target Market(s)

Companies - HR and Finance

Industry/Entity Type

Employee

Requirements
Must have
• Map of world or globe

```html
<!DOCTYPE html>
<html lang="en">
<head>
<meta charset="utf-8">
<title>Halvorsen Global – Results Oriented Approach</title>
<link rel="stylesheet" href="https://fonts.googleapis.com/css2?family=Oswald:wght@300;400;500;700&family=Arimo:wght@400&family=PT+Sans:wght@400&display=swap">
<style>
:root{
  --ink:#111;
  --nav:#555;
  --muted:#8a8a8a;
  --text:#555;
  --green:#9cc35f;
  --box-deep:#8bbacb;
  --box-light:#c2dfe9;
  --box-grey:#d0dcdf;
  --rule:#e6e6e6;
  --white:#fff;
}
*{margin:0;padding:0;box-sizing:border-box}
html,body{width:1200px;height:1171px;overflow:hidden;background:var(--white)}
.page{position:relative;width:1200px;height:1171px;font-family:"Arimo",Arial,sans-serif;color:var(--ink)}

.brand{position:absolute;left:198px;top:58px;width:218px}
.brand-name{position:absolute;left:0;top:0;font-family:"Oswald",sans-serif;font-weight:400;font-size:34px;line-height:40px;letter-spacing:-0.6px;color:var(--ink);white-space:nowrap}
.brand-tagline{position:absolute;right:0;top:44px;font-family:"Oswald",sans-serif;font-weight:300;font-size:13px;color:var(--muted);white-space:nowrap}

.social{position:absolute;left:310px;top:133px;display:flex;gap:6px}
.social span{width:21px;height:21px;border-radius:50%;border:1.5px solid #9a9a9a}

.nav{position:absolute;left:578px;top:80px;display:flex;align-items:center}
.nav a{font-family:"Oswald",sans-serif;font-weight:400;font-size:15.5px;color:var(--nav);text-decoration:none;text-transform:uppercase;padding:0 13px;line-height:24px;border-left:1px dotted #c8c8c8}
.nav a:first-child{border-left:none;padding-left:0}
.nav a:last-child{padding-right:0}

.globe{position:absolute;left:398px;top:167px;width:420px;height:377px;border-radius:50%;
  background:radial-gradient(circle at 50% 45%,rgba(226,238,244,.9) 0%,rgba(168,196,216,.75) 45%,rgba(190,205,225,.45) 70%,rgba(255,255,255,0) 72%)}

.hero-banner{position:absolute;left:263px;top:340px;width:689px;height:101px;border-radius:3px;
  background:repeating-linear-gradient(135deg,var(--green) 0 3px,#96bd59 3px 5px);box-shadow:0 1px 2px rgba(0,0,0,.15)}
.hero-arrow{position:absolute;top:32px;width:36px;height:36px;border-radius:50%;
  background:radial-gradient(circle at 50% 40%,#8cc14c,#4d7d1f);box-shadow:0 0 0 2px #7aa548,inset 0 1px 2px rgba(255,255,255,.4)}
.hero-arrow.prev{left:20px}
.hero-arrow.next{right:20px}
.hero-arrow svg{position:absolute;left:11px;top:11px}
.hero-title{position:absolute;right:124px;top:6px;text-align:right;font-family:"Oswald",sans-serif;font-weight:400;text-transform:uppercase;letter-spacing:-0.5px}
.hero-title .line-one{display:block;font-size:37px;line-height:44px;color:var(--ink)}
.hero-title .line-two{display:block;font-size:50px;line-height:48px;color:var(--white);margin-top:-4px}

.features{position:absolute;left:198px;top:580px;display:flex;gap:7px}
.feature{position:relative;width:268px;height:243px;border-radius:4px;text-align:center;box-shadow:0 12px 12px -8px rgba(0,0,0,.18)}
.feature.strategies{background:var(--box-deep)}
.feature.research{background:var(--box-light)}
.feature.solutions{background:var(--box-grey)}
.feature h2{margin-top:18px;font-family:"Oswald",sans-serif;font-weight:400;font-size:24px;line-height:32px;text-transform:uppercase;color:var(--ink);letter-spacing:-0.3px}
.feature svg{display:block;margin:10px auto 0;filter:drop-shadow(2px 3px 2px rgba(0,0,0,.2))}
.feature p{position:absolute;left:44px;right:44px;top:185px;font-size:11px;line-height:14px;letter-spacing:0.3px;color:#222}

.welcome{position:absolute;left:0;width:1200px;top:852px;text-align:center;font-family:"Oswald",sans-serif;font-weight:700;font-size:78px;line-height:84px;letter-spacing:-1px;color:var(--ink)}
.intro{position:absolute;left:236px;width:746px;top:953px;text-align:center;font-family:"PT Sans",sans-serif;font-size:12.6px;line-height:15.5px;color:var(--text)}
.more-button{position:absolute;left:514px;top:1018px;width:189px;height:49px;border-radius:4px;background:linear-gradient(#4d4d4d,#333);
  font-family:"Oswald",sans-serif;font-size:24px;line-height:49px;text-align:center;color:var(--white);text-decoration:none;text-transform:uppercase}

.footer{position:absolute;left:198px;top:1098px;width:810px;border-top:1px dotted var(--rule)}
.footer-links{position:absolute;left:1px;top:19px;font-size:11px;color:#555;white-space:nowrap}
.footer-links a{color:#555;text-decoration:none}
.copyright{position:absolute;right:5px;top:19px;font-size:11px;line-height:14px;color:var(--muted)}
</style>
</head>
<body>
<div class="page">
  <header>
    <div class="brand">
      <div class="brand-name">Halvorsen Global</div>
      <div class="brand-tagline">Results Oriented Approach</div>
    </div>
    <div class="social" aria-label="Social links">
      <span></span><span></span><span></span><span></span>
    </div>
    <nav class="nav">
      <a href="#">About Us</a>
      <a href="#">Resourses</a>
      <a href="#">Expertise</a>
      <a href="#">References</a>
      <a href="#">Contact Us</a>
    </nav>
  </header>

  <div class="globe" role="img" aria-label="Globe built from soft blue and grey tiles signifying global success"></div>

  <section class="hero-banner">
    <a class="hero-arrow prev" href="#" aria-label="Previous">
      <svg width="14" height="14" viewBox="0 0 14 14"><path d="M10 2 L3 7 L10 12 Z" fill="#b9dc8c"/></svg>
    </a>
    <h1 class="hero-title">
      <span class="line-one">Change your future with us!</span>
      <span class="line-two">Be successful!</span>
    </h1>
    <a class="hero-arrow next" href="#" aria-label="Next">
      <svg width="14" height="14" viewBox="0 0 14 14"><path d="M4 2 L11 7 L4 12 Z" fill="#b9dc8c"/></svg>
    </a>
  </section>

  <section class="features">
    <article class="feature strategies">
      <h2>Customized Strategies</h2>
      <svg width="110" height="110" viewBox="0 0 110 110" aria-hidden="true">
        <circle cx="48" cy="62" r="42" fill="#fff"/>
        <circle cx="48" cy="62" r="31" fill="var(--box-deep)"/>
        <circle cx="48" cy="62" r="24" fill="#fff"/>
        <circle cx="48" cy="62" r="15" fill="var(--box-deep)"/>
        <circle cx="48" cy="62" r="9" fill="#fff"/>
        <path d="M48 62 L92 20" stroke="#fff" stroke-width="5" stroke-linecap="round"/>
        <path d="M84 14 L86 28 L100 26 L104 10 L92 8 Z" fill="#fff"/>
      </svg>
      <p>Beciegast nveriti vitaesaert asety kertya aset aplicabrde ertyas nemo eniptaiades.</p>
    </article>
    <article class="feature research">
      <h2>Our Research</h2>
      <svg width="110" height="110" viewBox="0 0 110 110" aria-hidden="true">
        <g fill="#fff">
          <circle cx="30" cy="28" r="16"/>
          <g stroke="#fff" stroke-width="7"><path d="M30 6 V50 M8 28 H52 M14 12 L46 44 M46 12 L14 44"/></g>
          <circle cx="70" cy="66" r="28"/>
          <g stroke="#fff" stroke-width="10"><path d="M70 30 V102 M34 66 H106 M45 41 L95 91 M95 41 L45 91"/></g>
          <circle cx="20" cy="74" r="11"/>
          <g stroke="#fff" stroke-width="5"><path d="M20 58 V90 M4 74 H36 M9 63 L31 85 M31 63 L9 85"/></g>
        </g>
        <circle cx="30" cy="28" r="8" fill="var(--box-light)"/>
        <circle cx="70" cy="66" r="17" fill="var(--box-light)"/>
        <circle cx="20" cy="74" r="5" fill="var(--box-light)"/>
      </svg>
      <p>Asety kscabo nerafaes kertyu ersvitae ertyasnemo lasec vasptaiades goertayse.</p>
    </article>
    <article class="feature solutions">
      <h2>Solutions</h2>
      <svg width="110" height="110" viewBox="0 0 110 110" aria-hidden="true">
        <circle cx="72" cy="32" r="26" fill="#fff"/>
        <circle cx="78" cy="26" r="7" fill="var(--box-grey)"/>
        <path d="M56 46 L14 92 L22 100 L30 92 L36 98 L42 92 L36 86 L46 76 L52 82 L58 76 L52 70 L66 54 Z" fill="#fff"/>
      </svg>
      <p>Miiasrdas nveriti vitaesaert aplicabrdasety kertya asee ertyas nemo eniptaiades.</p>
    </article>
  </section>

  <h2 class="welcome">WELCOME</h2>
  <p class="intro">Halvorsen Global brings a results oriented approach partnering with clients in mapping out customized strategies that meet their international objectives that save time and money and leaves an established process in place. &nbsp;The client is supported with a high touch, one point of contact, that bring solutions to complex problems</p>
  <a class="more-button" href="#">More Details</a>

  <footer class="footer">
    <div class="footer-links">
      <a href="#">Home</a> - <a href="#">Resourses</a> - <a href="#">Expertise</a> - <a href="#">References</a> - <a href="#">Contact us</a>
    </div>
    <div class="copyright">© 2013 Halvorsen Global.com<br>All Rights Reserved</div>
  </footer>
</div>
</body>
</html>
```